Fiscal Sponsorship Program Flyer

We are seeking a designer to create a 1-2 flyer that explains our fiscal sponsorship program. This flyer will be used to recruit new projects that might be interested in utilizing our fiscal sponsorship services. The pertinent information about our program can be found in the attached PDF. For users who cannot access the PDF, please try this link: https://files.plovarimedia.net/deck/7QtR2wzoLkVa9pXcJ4nEuYhsT3bGdMf8eKqW5rZxN1yo/view?mode=public

Target Market(s)

New charitable projects that do not yet have their own 501(c)(3) status, and are seeking a fiscal sponsor.

Industry/Entity Type

Nonprofit/Charity

Requirements
Must have
• The flyer must include the language and detail included on the attached PDF. The desire is to reformat this to be more appealing and easy to read.

```html
<!DOCTYPE html>
<html lang="en">
<head>
<meta charset="utf-8">
<title>Meridian Foundation – Fiscal Sponsorship Program Flyer</title>
<link rel="stylesheet" href="https://fonts.googleapis.com/css2?family=Tinos:wght@400;700&family=Raleway:wght@400;500;600;700;800&display=swap">
<style>
:root{
  --stage:#464646;
  --paper:#ffffff;
  --pink:#f57d85;
  --red:#e9505a;
  --ink:#2e2f33;
  --text:#3a3a3a;
  --card-gray:#cbcdcf;
  --label-gray:#9b9c9e;
  --dot-gray:#b9babc;
  --icon-gray:#8c8d90;
}
*{box-sizing:border-box;margin:0;padding:0}
html,body{width:1200px;height:989px;overflow:hidden;background:var(--stage)}
body{position:relative;font-family:"Raleway",Arial,sans-serif;color:var(--text)}
.serif{font-family:"Tinos","Times New Roman",serif}
.page{position:absolute;top:121px;width:530px;height:749px;background:var(--paper);overflow:hidden}
.page--intro{left:47px}
.page--fees{left:621px}

/* ---------- intro page ---------- */
.hero{position:absolute;left:0;top:0;width:530px;height:190px;
  background:linear-gradient(115deg,#e8eaec 0%,#c6cacd 30%,#eef0f1 55%,#b9bec2 75%,#e4e6e8 100%)}
.lower-band{position:absolute;left:0;top:399px;width:530px;height:350px;background:var(--pink)}
.title{position:absolute;left:0;width:530px;text-align:center;color:var(--ink);font-weight:700}
.title--main{top:30px;font-size:49px;letter-spacing:.3px}
.title--sub{top:86px;font-size:30px}
.pill{position:absolute;left:154px;top:141px;width:222px;height:35px;background:var(--ink);border-radius:6px;
  color:#fff;font-size:23px;font-weight:700;text-align:center;line-height:35px}
.mission{position:absolute;left:32px;top:159px;width:466px;height:88px;background:var(--pink);border-radius:4px;
  display:flex;padding:26px 16px 0 20px;color:#fff;font-size:8.4px;font-weight:600;line-height:12.4px}
.mission p{flex:1}
.mission .divider{width:1px;background:#fff;margin:0 10px;height:45px;margin-top:-2px}
.section-title{position:absolute;left:0;width:530px;text-align:center;color:var(--ink);font-weight:700;font-size:22px}
.lead{position:absolute;left:40px;top:285px;width:450px;text-align:center;font-size:8.4px;line-height:12.2px;font-weight:500}
.info-card{position:absolute;top:343px;height:216px;background:var(--card-gray);border-radius:8px;padding:14px 12px}
.info-card--eligible{left:32px;width:224px}
.info-card--philosophy{left:266px;width:230px}
.info-card h3{font-family:"Tinos","Times New Roman",serif;font-size:14px;line-height:15.5px;color:var(--ink)}
.info-card .rule{height:2px;background:var(--red);margin:8px 0 14px;width:100%;position:relative}
.info-card .rule::before{content:"";position:absolute;left:0;top:-1px;width:66px;height:4px;background:#c24550}
.info-card p{font-size:8.3px;line-height:11.4px;font-weight:500;margin-bottom:8px}
.checks{list-style:none}
.checks li{display:flex;gap:8px;font-size:8.3px;line-height:11.4px;font-weight:500;margin-bottom:8px}
.checks svg{flex:none;margin-top:1px}
.values-head{position:absolute;left:32px;top:578px;width:466px;display:flex;align-items:center;gap:12px}
.values-head .line{flex:1;height:2px;background:var(--ink)}
.values-head h2{color:#fff;font-size:22px;font-weight:700}
.value{position:absolute;display:flex;gap:9px;font-size:8.3px;line-height:11.4px;font-weight:500;color:#fff}
.value b{color:var(--ink);font-weight:800}
.value .icon{flex:none;width:20px;height:20px;border-radius:50%;background:var(--icon-gray);display:flex;align-items:center;justify-content:center}

/* ---------- fees page ---------- */
.fees-hero{position:absolute;left:0;top:0;width:530px;height:285px;
  background:linear-gradient(160deg,#f7f7f8 0%,#eceeef 50%,#f4f5f6 100%)}
.commit-title{position:absolute;left:33px;top:30px;color:var(--red);font-size:22px;font-weight:700}
.commit-col{position:absolute;top:70px;list-style:none}
.commit-col--left{left:33px;width:205px}
.commit-col--right{left:272px;width:230px}
.commit-col li{display:flex;gap:9px;font-size:10.3px;line-height:14.5px;color:var(--text);margin-bottom:13px}
.commit-col svg{flex:none;margin-top:2px}
.commit-divider{position:absolute;left:251px;top:74px;width:2px;height:155px;background:var(--pink)}
.fee-banner{position:absolute;left:117px;top:253px;width:296px;height:40px;background:var(--pink);border-radius:8px;
  text-align:center;line-height:40px;font-size:27px;font-weight:700;color:var(--ink)}
.tier{position:absolute;top:307px;width:152px;height:423px;background:var(--pink);border-radius:8px;padding:20px 0 0 20px;color:#fff}
.tier--basic{left:31px}
.tier--standard{left:187px;padding-left:16px}
.tier--premium{left:343px;padding-left:21px}
.tier h3{font-family:"Tinos","Times New Roman",serif;font-size:24px;line-height:28px;font-weight:700;white-space:nowrap}
.tier .label{width:115px;height:22px;background:var(--label-gray);margin:15px 0 12px;font-size:12px;font-weight:700;line-height:22px;padding-left:16px}
.tier .label--center{padding-left:0;text-align:center}
.tier .caps{font-size:10px;font-weight:800;margin-bottom:8px;line-height:14px}
.tier .note{font-size:10.3px;line-height:14.8px;font-weight:500;margin-bottom:14px;padding-right:6px}
.tier ul{list-style:none}
.tier li{position:relative;padding-left:20px;font-size:10.3px;line-height:14.8px;font-weight:600;margin-bottom:9.5px}
.tier li::before{content:"";position:absolute;left:2px;top:4px;width:6px;height:6px;border-radius:50%;background:var(--dot-gray)}
.tier--standard li{margin-bottom:15px}
</style>
</head>
<body>

<svg width="0" height="0" style="position:absolute" aria-hidden="true">
  <symbol id="tick" viewBox="0 0 12 12">
    <circle cx="6" cy="6" r="6" fill="#e9505a"/>
    <path d="M3.3 6.2l1.8 1.8 3.6-3.7" fill="none" stroke="#fff" stroke-width="1.5" stroke-linecap="round" stroke-linejoin="round"/>
  </symbol>
</svg>

<!-- Page one: introduction -->
<section class="page page--intro">
  <div class="hero" role="img" aria-label="Soft grey photograph of a handshake behind the title"></div>
  <div class="lower-band"></div>

  <h1 class="title title--main serif">Meridian Foundation</h1>
  <div class="title title--sub serif">Fiscal Sponsorship Program</div>

  <div class="mission">
    <p>The Meridian Foundation, founded in 2010, exists to support social impact campaigns and organizations through educational, public engagement, and awareness efforts.</p>
    <span class="divider"></span>
    <p>Its vision is to strengthen the capacity of the social impact sector and its leaders by providing top-tier fiscal sponsorship services.</p>
  </div>
  <div class="pill serif">Mission &amp; Vision</div>

  <h2 class="section-title serif" style="top:253px">What is Fiscal Sponsorship?</h2>
  <p class="lead">Fiscal sponsorship refers to the practice of non-profit organizations offering their legal and tax-exempt status to charitable projects or groups engaged in activities related to the sponsoring organization's mission. Fiscal sponsors provide oversight, financial management, and other administrative services to build the capacity of charitable projects.</p>

  <div class="info-card info-card--eligible">
    <h3>What kinds of projects are eligible for fiscal sponsorship?</h3>
    <div class="rule"></div>
    <p>Meridian Foundation uses the following broad criteria to determine whether or not a project is eligible for fiscal sponsorship:</p>
    <ul class="checks">
      <li><svg width="10" height="10"><use href="#tick"/></svg><span>Mission alignment with the Meridian Foundation;</span></li>
      <li><svg width="10" height="10"><use href="#tick"/></svg><span>Whether or not the project provides an educational, social or charitable benefit; and</span></li>
      <li><svg width="10" height="10"><use href="#tick"/></svg><span>Whether or not the project's activities follow the IRS regulations governing 501© (3) public charities.</span></li>
    </ul>
  </div>

  <div class="info-card info-card--philosophy">
    <h3>Fiscal Sponsorship Program Philosophy</h3>
    <div class="rule"></div>
    <p>We believe we can accelerate the pace and scale of social change by providing strategic back office support to emerging projects, leaders and ideas.</p>
    <p>By providing light touch administrative and capacity building services, our fiscal sponsorship program takes the administrative burden off the shoulders of leaders and their projects to allow them to focus on what they do best - achieving impact and changing the world.</p>
  </div>

  <div class="values-head">
    <span class="line"></span>
    <h2 class="serif">Organizational Values</h2>
    <span class="line"></span>
  </div>

  <div class="value" style="left:35px;top:616px;width:225px">
    <span class="icon"><svg width="10" height="10"><circle cx="5" cy="5" r="3" fill="#fff"/></svg></span>
    <p><b>TRUST:</b> We believe that all successful partnerships begin with a foundation of trust.</p>
  </div>
  <div class="value" style="left:35px;top:650px;width:225px">
    <span class="icon"><svg width="10" height="10"><circle cx="5" cy="5" r="3" fill="#fff"/></svg></span>
    <p><b>INNOVATION:</b> We embrace continuous improvement, bold creativity and change.</p>
  </div>
  <div class="value" style="left:35px;top:684px;width:225px">
    <span class="icon"><svg width="10" height="10"><circle cx="5" cy="5" r="3" fill="#fff"/></svg></span>
    <p><b>EMBRACE COMPLEXITY AND RISK:</b> We understand that bold solutions to intractable social issues often require both complexity and risk.</p>
  </div>
  <div class="value" style="left:285px;top:616px;width:215px">
    <span class="icon"><svg width="10" height="10"><circle cx="5" cy="5" r="3" fill="#fff"/></svg></span>
    <p><b>DIVERSITY:</b> We believe that all voices matter and that effective solutions are created when decision-making is inclusive across social, cultural and economic backgrounds.</p>
  </div>
  <div class="value" style="left:285px;top:684px;width:215px">
    <span class="icon"><svg width="10" height="10"><circle cx="5" cy="5" r="3" fill="#fff"/></svg></span>
    <p><b>RELATIONSHIPS:</b> Our partners are central to our work. We honor our relationships through respect, communication and transparency.</p>
  </div>
</section>

<!-- Page two: commitments and fees -->
<section class="page page--fees">
  <div class="fees-hero" role="img" aria-label="Faint pale grey hexagon pattern background"></div>

  <h2 class="commit-title serif">Meridian Foundation - Program Commitments</h2>

  <ul class="commit-col commit-col--left">
    <li><svg width="10" height="10"><use href="#tick"/></svg><span>Fast, simple and efficient fiscal sponsorship program</span></li>
    <li><svg width="10" height="10"><use href="#tick"/></svg><span>No fees and no minimums; projects of any size are welcome to apply</span></li>
    <li><svg width="10" height="10"><use href="#tick"/></svg><span>Easy onboarding process</span></li>
    <li><svg width="10" height="10"><use href="#tick"/></svg><span>Complex, hybrid structures, partnerships and coalitions are strongly encouraged to apply</span></li>
  </ul>
  <span class="commit-divider"></span>
  <ul class="commit-col commit-col--right">
    <li><svg width="10" height="10"><use href="#tick"/></svg><span>Free and fast approval process - our application can be completed in 30 minutes or less. There is no fee to apply, and most projects can expect to receive a response on their application within 2 weeks</span></li>
    <li><svg width="10" height="10"><use href="#tick"/></svg><span>Dedicated customer service and customization of services, tailored to the individual sponsored project's needs</span></li>
  </ul>

  <div class="fee-banner serif">FEE STRUCTURE</div>

  <div class="tier tier--basic">
    <h3>Basic |<br>Fee - 4%</h3>
    <div class="label">Limited</div>
    <ul>
      <li>Project Fund Set-Up</li>
      <li>Administration and Management</li>
      <li>Financial Management</li>
      <li>Grant Proposal Review</li>
      <li>Grant Contract Review</li>
      <li>Project Reporting</li>
      <li>Insurance</li>
      <li>Annual Audit and Form 990</li>
    </ul>
  </div>

  <div class="tier tier--standard">
    <h3>Standard |<br>Fee - 6%</h3>
    <div class="label label--center">Comprehensive</div>
    <div class="caps">BASIC SERVICES +</div>
    <ul>
      <li>Customized Financial Reporting</li>
      <li>Monthly Financial Statements</li>
      <li>Subgranting/ regranting to U.S.-based organizations</li>
      <li>Management of Vendor and Independent Contractors (1099s)</li>
    </ul>
  </div>

  <div class="tier tier--premium">
    <h3>Premium |<br>Fee - 10% +</h3>
    <div class="label label--center">Custom</div>
    <p class="note">Standard Services + custom services tailored to individual project needs.</p>
    <div class="caps">CUSTOMIZATION OPTIONS:</div>
    <ul>
      <li>Subgranting/ regranting to international organizations</li>
      <li>Lobbying Filings</li>
      <li>Project Audit</li>
      <li>Grant Writing Assistance</li>
      <li>One-on-One Coaching</li>
    </ul>
  </div>
</section>

</body>
</html>
```